UK Speciality Product Manufacturer Needs Quality Bottle Label For Pet Urine Odour Remover Product

We are looking for a professional bottle label design for our pet urine odour remover product.
This will be the initial steps of a much larger project which will eventually cover our full product range.
Ideally show our logo on the label as we want to build a corporate image for the business throughout our product range.
Labels should reflect top quality and outstanding performance of the product, definitely not cheap bargain price. Our market is to every pet owner dog/cat, etc; but we also supply vets, kennels, catteries, dog walkers and the whole pet care industry throughout the UK. Environmentally friendly and safe.
Would like to keep label fairly simple but stress effectiveness, safe enzymes and natural aspects of product.
I have attached a copy of our logo and details of our current label which is old and now completely unsuitable, but it shows more information about the product.
Label size required: 13cm high x 24cm wide.

Target Market(s)

Pet Care

Industry/Entity Type

Pet Care

Requirements
Must have
• Suitable for applying to white plastic bottles (see attached)

The following text on the back of bottle:

PET URINE ODOUR & STAIN REMOVER
Loram-X6 is a super strength biological formulation containing a complex blend of enzymes and bacteria designed to attack bacterial waste and pet urine in carpets, fabrics & hard surfaces and remove it by digestive action.
Dilutes up to 10 : 1 with water.
Do not use with disinfectants.

DIRECTIONS
Loram-X6 must be diluted before use. Simply add the concentrate to the trigger spray bottle to the level required and top up with warm water. The enzymes are activated when the water is added and the product can then be used. First dab the area with absorbent paper to remove any excess urine and waste.
Loram-X6 can then be applied by simply spraying or by dabbing onto the affected area to wet/moisten the surface, then allow sufficient time for Loram-X6 to dry out slowly and naturally.
The process can be repeated if necessary over 2 - 3 days until all of the odours and stains have been completely digested but usually only one application should be required.
Only make up sufficient product for one application and discard remaining contents after use. Product only remains active for 24 hrs so a fresh solution will be needed for further applications.

For professional / commercial / industrial use.

NOT CLASSIFIED AS HAZARDOUS

HEALTH AND SAFETY INFORMATION
Keep out of reach of children. Avoid contact with skin and eyes.
If swallowed seek medical advice and show this label.
Nice to have
• Cat & Dog image in background would be nice.

```html
<!DOCTYPE html>
<html lang="en">
<head>
<meta charset="utf-8">
<title>Loram-X6 Super Strength Label</title>
<link rel="stylesheet" href="https://fonts.googleapis.com/css2?family=Montserrat:wght@300;400;500;600;700&display=swap">
<style>
  :root {
    --page: #ffffff;
    --label: #050505;
    --accent: #f29a12;
    --ink: #ffffff;
    --ink-soft: #e6e6e6;
    --photo-light: #e9e9e9;
    --photo-dark: #5a5a5a;
    --divider: #1a1a1a;
  }
  * { box-sizing: border-box; margin: 0; padding: 0; }
  html, body {
    width: 875px; height: 1200px; overflow: hidden;
    background: var(--page);
    font-family: "Montserrat", sans-serif;
  }
  .canvas { position: relative; width: 875px; height: 1200px; }
  .label {
    position: absolute; left: 17px; top: 371px;
    width: 840px; height: 457px;
    background: var(--label);
    box-shadow: 0 10px 28px rgba(0,0,0,.35);
    display: flex; overflow: hidden;
  }
  .front { position: relative; width: 417px; height: 100%; border-right: 1px solid var(--divider); }
  .back { position: relative; flex: 1; height: 100%; text-align: center; color: var(--ink-soft); }

  .brand { display: flex; flex-direction: column; align-items: center; color: var(--ink); font-weight: 700; }
  .brand-dot { border-radius: 50%; background: var(--ink); }
  .front .brand { position: absolute; left: 30px; top: 36px; }
  .front .brand-dot { width: 44px; height: 44px; margin-bottom: 10px; }
  .front .brand-name { font-size: 13px; letter-spacing: .5px; }
  .back .brand { margin: 22px auto 0; }
  .back .brand-dot { width: 26px; height: 26px; margin-bottom: 6px; }
  .back .brand-name { font-size: 8px; letter-spacing: .4px; }

  .product-name {
    position: absolute; left: 30px; top: 172px;
    width: 156px;
    color: var(--accent); font-weight: 600;
    font-size: 44px; line-height: 1; letter-spacing: -1.5px;
    white-space: nowrap;
  }
  .strength { position: absolute; left: 29px; top: 273px; color: var(--ink); font-weight: 400; font-size: 13.5px; letter-spacing: .3px; }
  .volume { position: absolute; left: 37px; top: 420px; color: var(--ink); font-weight: 400; font-size: 12.5px; }
  .dog-photo { position: absolute; left: 192px; top: 118px; width: 222px; height: 339px; }

  .back-title { color: var(--accent); font-weight: 600; font-size: 28px; margin-top: 10px; line-height: 1; }
  .copy { width: 340px; margin: 8px auto 0; font-weight: 300; font-size: 8.3px; line-height: 1.32; }
  .copy p + p { margin-top: 9px; }
  .copy .key { font-weight: 600; color: var(--ink); font-size: 8.6px; }
  .fine { width: 340px; margin: 18px auto 0; font-size: 5.2px; line-height: 1.4; }
  .fine p + p { margin-top: 7px; }
  .fine strong { font-weight: 600; color: var(--ink); }
</style>
</head>
<body>
<div class="canvas">
  <section class="label">
    <div class="front">
      <div class="brand"><span class="brand-dot"></span><span class="brand-name">NORVALE</span></div>
      <h1 class="product-name">LORAM<br>X6</h1>
      <p class="strength">SUPER STRENGTH</p>
      <svg class="dog-photo" viewBox="0 0 222 339" role="img" aria-label="Black and white photograph of a happy terrier dog looking upward">
        <defs>
          <linearGradient id="dogTone" x1="0" y1="0" x2="0.4" y2="1">
            <stop offset="0" stop-color="var(--photo-dark)"/>
            <stop offset="0.45" stop-color="#9a9a9a"/>
            <stop offset="1" stop-color="var(--photo-light)"/>
          </linearGradient>
        </defs>
        <rect width="222" height="339" fill="url(#dogTone)"/>
      </svg>
      <p class="volume">1 Litre</p>
    </div>
    <div class="back">
      <div class="brand"><span class="brand-dot"></span><span class="brand-name">NORVALE</span></div>
      <h2 class="back-title">LORAM X6</h2>
      <div class="copy">
        <p>Loram-X6 is a super strength biological formulation containing a complex blend of enzymes and bacteria designed to attack bacterial waste and pet urine in carpets, fabrics &amp; hard surfaces and remove it by digestive action.</p>
        <p class="key">Dilutes up to 10 : 1 with water<br>Do not use with disinfectants</p>
        <p>Loram-X6 must be diluted before use. Simply add the concentrate to the trigger spray bottle to the level required and top up with warm water. The enzymes are activated when the water is added and the product can then be used. First dab the area with absorbent paper to remove any excess urine and waste.<br>Loram-X6 can then be applied by simply spraying or by dabbing onto the affected area to wet/moisten the surface, then allow sufficient time for Loram-X6 to dry out slowly and naturally.</p>
        <p>The process can be repeated if necessary over 2 - 3 days until all of the odours and stains have been completely digested but usually only one application should be required.</p>
        <p>Only make up sufficient product for one application and discard remaining contents after use. Product only remains active for 24 hrs so a fresh solution will be needed for further applications</p>
      </div>
      <div class="fine">
        <p><strong>For professional / commercial / industrial use.</strong></p>
        <p>NOT CLASSIFIED AS HAZARDOUS</p>
        <p><strong>HEALTH AND SAFETY INFORMATION</strong><br>Keep out of reach of children. Avoid contact with skin and eyes.<br>If swallowed seek medical advice and show this label</p>
      </div>
    </div>
  </section>
</div>
</body>
</html>
```